"Use it or Lose it" and "Brush on Over"

We are a dental office looking to connect with our patients through direct mail advertising. With the last 3 months of the year coming we would like to send out Post Cards to our patients letting them know they have 3 months left to "USE IT OR LOSE IT" when it comes to their dental insurance benefits.
So we are looking for a post card that has the "Use It or Lost it" theme along with our dental office logo, telephone number and address.

We are also looking for a post card that says "Brush On Over" to remind our patients that they are due for a dental cleaning and we would like for them to come over to our dental office for a well needed cleaning :).

```html
<!DOCTYPE html>
<html lang="en">
<head>
<meta charset="utf-8">
<title>Linden Dental Postcards</title>
<link href="https://fonts.googleapis.com/css2?family=Poppins:wght@400;500;600;700&display=swap" rel="stylesheet">
<style>
:root{
  --navy:#13325a;
  --green:#9ccb3b;
  --orange:#f7941d;
  --white:#ffffff;
  --brand-blue:#2a8ad4;
  --board-top:#a8a8a8;
  --board-bottom:#b9b9b9;
  --label:#2d3e55;
  --option-two:#5a7396;
}
*{margin:0;padding:0;box-sizing:border-box}
html,body{width:1200px;height:984px;overflow:hidden}
body{font-family:"Poppins",sans-serif;position:relative;background:var(--board-bottom)}
.band-top{position:absolute;left:0;top:0;width:1200px;height:500px;background:var(--board-top)}
.option-tag{position:absolute;font-weight:600;font-size:21px;transform:rotate(-90deg);transform-origin:left top;white-space:nowrap}
.option-one{left:14px;top:304px;color:var(--white)}
.option-two{left:14px;top:760px;color:var(--option-two)}
.side-label{position:absolute;font-size:28px;color:var(--label);transform:translateX(-50%)}
.card{position:absolute;width:536px;height:380px;overflow:hidden;background:var(--navy)}
.card > svg{position:absolute;left:0;top:0}
.abs{position:absolute}
.brand{display:flex;align-items:center;gap:6px;font-weight:600;color:var(--navy);font-size:17px;letter-spacing:.5px;white-space:nowrap}
.brand .dot{width:14px;height:14px;border-radius:50%;background:var(--brand-blue)}
.brand.on-dark{color:var(--brand-blue)}
.bubble{position:absolute;width:86px;height:86px;border-radius:50%;background:var(--white)}
.head{font-weight:700;color:var(--white);line-height:.9;letter-spacing:-1px;white-space:nowrap}
.head-row{display:flex;align-items:baseline;gap:6px}
.green{color:var(--green)}
.orange{color:var(--orange)}
.small{font-size:8.4px;font-weight:500;color:var(--white);line-height:10.7px;white-space:nowrap}
.rule{position:absolute;height:1.5px;background:var(--white)}
.contact{position:absolute;display:flex;align-items:center;gap:6px;font-size:12px;font-weight:600;color:var(--navy);white-space:nowrap}
.contact .ico{width:11px;height:11px}
.contact .gap{width:8px}
.stamp{position:absolute;border:1.5px dashed #888;padding:4px}
.stamp span{display:block;width:100%;height:100%;border:1px solid #888}
.to{position:absolute;font-size:11px;font-weight:600;color:#222}
.addr-line{position:absolute;height:1px;background:#222;width:168px}
.cal{position:absolute;width:52px;height:58px;border:2px solid var(--white);border-radius:3px}
.cal .rings{position:absolute;top:-8px;left:6px;display:flex;gap:6px}
.cal .rings i{display:block;width:8px;height:10px;border:2px solid var(--white);border-radius:4px}
.cal .month{position:absolute;top:4px;left:0;width:100%;background:var(--white);color:var(--navy);font-size:8px;font-weight:600;text-align:center;line-height:11px}
.cal .day{position:absolute;top:16px;left:0;width:100%;text-align:center;color:var(--white);font-weight:700;font-size:26px;line-height:36px}
.cal .day sup{font-size:10px;vertical-align:top;line-height:22px}
.expire{position:absolute;font-size:9.5px;font-weight:500;color:var(--white)}
</style>
</head>
<body>
<div class="band-top"></div>
<div class="option-tag option-one">Option 01</div>
<div class="option-tag option-two">Option 02</div>

<!-- Option 01 front -->
<div class="card" style="left:47px;top:67px">
  <svg width="536" height="380">
    <defs>
      <clipPath id="family-area"><path d="M425,0 C300,70 175,200 130,380 L536,380 L536,0 Z"/></clipPath>
      <radialGradient id="family-tone" cx="62%" cy="55%" r="60%">
        <stop offset="0" stop-color="#d9b49a"/><stop offset=".5" stop-color="#ead8ca"/><stop offset="1" stop-color="#ffffff"/>
      </radialGradient>
    </defs>
    <path d="M425,0 C300,70 175,200 130,380 L536,380 L536,0 Z" fill="#fff"/>
    <g role="img" aria-label="Photo of a smiling family of four hugging" clip-path="url(#family-area)">
      <rect x="150" y="140" width="386" height="240" fill="url(#family-tone)"/>
    </g>
  </svg>
  <div class="bubble" style="left:278px;top:41px"></div>
  <div class="brand abs" style="left:300px;top:70px"><span class="dot"></span>LINDEN DENTAL</div>
  <div class="head abs" style="left:57px;top:44px;font-size:56px">Brush</div>
  <div class="head abs green" style="left:57px;top:96px;font-size:42px">On Over</div>
  <div class="small abs" style="left:58px;top:158px">Don't Let Your<br><span class="green">Dental Insurance Benefits</span><br><span class="orange">Go to Waste!</span></div>
  <div class="rule" style="left:58px;top:198px;width:74px"></div>
  <div class="small abs" style="left:58px;top:208px">Your teeth are important.<br>You use them to eat, and<br>your smile gives people<br>their first impression<br>of you. For such an<br>important part of<br>you, you'll want<br>only top-quality<br>experts to help<br>keep them in<br>the best shape<br>possible.</div>
  <div class="contact" style="left:190px;top:340px">
    <svg class="ico" viewBox="0 0 12 12"><circle cx="6" cy="6" r="6" fill="#13325a"/><path d="M4 3l1 1.5-.7.8c.4.9 1 1.5 1.9 1.9l.8-.7L8.5 7.5 7.8 8.8C5.5 8.5 3.5 6.5 3.2 4.2Z" fill="#fff"/></svg>555 - 014 - 2290<span class="gap"></span>
    <svg class="ico" viewBox="0 0 12 12"><circle cx="6" cy="6" r="6" fill="#13325a"/><circle cx="6" cy="6" r="2.5" fill="none" stroke="#fff" stroke-width="1.3"/></svg>www.LindenDental.com
  </div>
</div>

<!-- Option 01 back -->
<div class="card" style="left:618px;top:67px">
  <svg width="536" height="380"><path d="M316,0 C250,90 205,230 194,380 L536,380 L536,0 Z" fill="#fff"/></svg>
  <div class="brand on-dark abs" style="left:54px;top:40px;font-size:18px"><span class="dot"></span>LINDEN DENTAL</div>
  <div class="head abs" style="left:57px;top:78px;font-size:50px">Brush</div>
  <div class="head abs green" style="left:57px;top:125px;font-size:37px">On Over</div>
  <div class="rule" style="left:59px;top:166px;width:136px"></div>
  <div class="abs" style="left:59px;top:186px;font-size:23px;font-weight:600;line-height:31px;color:#fff">Its<br><span class="green">check up</span><br><span class="orange">time!</span></div>
  <div class="stamp" style="left:441px;top:26px;width:68px;height:59px"><span></span></div>
  <div class="to" style="left:334px;top:162px">TO:</div>
  <div class="addr-line" style="left:334px;top:201px"></div>
  <div class="addr-line" style="left:334px;top:230px"></div>
  <div class="addr-line" style="left:334px;top:261px"></div>
  <div class="contact" style="left:214px;top:340px">
    <svg class="ico" viewBox="0 0 12 12"><circle cx="6" cy="6" r="6" fill="#13325a"/><path d="M4 3l1 1.5-.7.8c.4.9 1 1.5 1.9 1.9l.8-.7L8.5 7.5 7.8 8.8C5.5 8.5 3.5 6.5 3.2 4.2Z" fill="#fff"/></svg>555 - 014 - 2290<span class="gap"></span>
    <svg class="ico" viewBox="0 0 12 12"><circle cx="6" cy="6" r="6" fill="#13325a"/><circle cx="6" cy="6" r="2.5" fill="none" stroke="#fff" stroke-width="1.3"/></svg>www.LindenDental.com
  </div>
</div>

<div class="side-label" style="left:322px;top:458px">Front</div>
<div class="side-label" style="left:878px;top:458px">Back</div>

<!-- Option 02 front -->
<div class="card" style="left:47px;top:521px">
  <svg width="536" height="380">
    <defs>
      <radialGradient id="clock-tone" cx="50%" cy="58%" r="55%">
        <stop offset="0" stop-color="#b7c3ae"/><stop offset=".7" stop-color="#8e9a88"/><stop offset=".85" stop-color="#2b2b2b"/><stop offset="1" stop-color="#1a1a1a"/>
      </radialGradient>
    </defs>
    <path d="M425,0 C300,70 175,200 130,380 L536,380 L536,0 Z" fill="#fff"/>
    <ellipse role="img" aria-label="Alarm clock with banknotes inside the dial" cx="384" cy="228" rx="78" ry="100" fill="url(#clock-tone)"/>
  </svg>
  <div class="bubble" style="left:278px;top:41px"></div>
  <div class="brand abs" style="left:300px;top:70px"><span class="dot"></span>LINDEN DENTAL</div>
  <div class="head abs" style="left:57px;top:46px;font-size:62px">Use</div>
  <div class="head abs head-row" style="left:57px;top:100px;font-size:44px">it <span class="green" style="font-size:64px">Or</span></div>
  <div class="head abs head-row" style="left:57px;top:156px;font-size:36px">Lose <span style="font-size:48px">it!</span></div>
  <div class="rule" style="left:58px;top:201px;width:74px"></div>
  <div class="abs" style="left:56px;top:210px;font-size:11px;font-weight:500;line-height:13.5px;color:#fff;white-space:nowrap">Just a<br>friendly reminder. ..<br><span class="green">it's time for your checkup.</span></div>
  <div class="cal" style="left:59px;top:271px"><div class="rings"><i></i><i></i><i></i></div><div class="month">December</div><div class="day">31<sup>st</sup></div></div>
  <div class="expire" style="left:58px;top:333px">Expiring on</div>
  <div class="contact" style="left:196px;top:340px">
    <svg class="ico" viewBox="0 0 12 12"><circle cx="6" cy="6" r="6" fill="#13325a"/><path d="M4 3l1 1.5-.7.8c.4.9 1 1.5 1.9 1.9l.8-.7L8.5 7.5 7.8 8.8C5.5 8.5 3.5 6.5 3.2 4.2Z" fill="#fff"/></svg>555 - 014 - 2290<span class="gap"></span>
    <svg class="ico" viewBox="0 0 12 12"><circle cx="6" cy="6" r="6" fill="#13325a"/><circle cx="6" cy="6" r="2.5" fill="none" stroke="#fff" stroke-width="1.3"/></svg>www.LindenDental.com
  </div>
</div>

<!-- Option 02 back -->
<div class="card" style="left:618px;top:521px">
  <svg width="536" height="380"><path d="M316,0 C250,90 205,230 194,380 L536,380 L536,0 Z" fill="#fff"/></svg>
  <div class="brand on-dark abs" style="left:54px;top:35px;font-size:18px"><span class="dot"></span>LINDEN DENTAL</div>
  <div class="head abs" style="left:57px;top:72px;font-size:60px">Use</div>
  <div class="head abs head-row" style="left:57px;top:124px;font-size:42px">it <span class="green" style="font-size:62px">Or</span></div>
  <div class="head abs head-row" style="left:57px;top:178px;font-size:34px">Lose <span style="font-size:46px">it!</span></div>
  <div class="rule" style="left:59px;top:229px;width:74px"></div>
  <div class="abs" style="left:58px;top:236px;font-size:10px;font-weight:500;line-height:13.5px;color:#fff">Its<br><span class="green">check up time!</span></div>
  <div class="cal" style="left:59px;top:283px;width:46px;height:50px"><div class="rings"><i></i><i></i><i></i></div><div class="month">December</div><div class="day" style="font-size:22px;line-height:32px">31<sup>st</sup></div></div>
  <div class="expire" style="left:58px;top:338px;font-size:9px">Expiring on</div>
  <div class="stamp" style="left:441px;top:26px;width:68px;height:59px"><span></span></div>
  <div class="to" style="left:334px;top:162px">TO:</div>
  <div class="addr-line" style="left:334px;top:201px"></div>
  <div class="addr-line" style="left:334px;top:230px"></div>
  <div class="addr-line" style="left:334px;top:261px"></div>
  <div class="contact" style="left:214px;top:340px">
    <svg class="ico" viewBox="0 0 12 12"><circle cx="6" cy="6" r="6" fill="#13325a"/><path d="M4 3l1 1.5-.7.8c.4.9 1 1.5 1.9 1.9l.8-.7L8.5 7.5 7.8 8.8C5.5 8.5 3.5 6.5 3.2 4.2Z" fill="#fff"/></svg>555 - 014 - 2290<span class="gap"></span>
    <svg class="ico" viewBox="0 0 12 12"><circle cx="6" cy="6" r="6" fill="#13325a"/><circle cx="6" cy="6" r="2.5" fill="none" stroke="#fff" stroke-width="1.3"/></svg>www.LindenDental.com
  </div>
</div>

<div class="side-label" style="left:322px;top:924px">Front</div>
<div class="side-label" style="left:878px;top:924px">Back</div>
</body>
</html>
```